Executive Business Card for Healthcare Company [Need Today]

I need a business card design for a healthcare company. The only branding the company has thus far is a logo. The cards will be utilized by company executives. The design I envision will be vibrant and appealing but with a corporate feel. They shouldn't be too casual or playful. I would like to complete this project TODAY if possible.

Target Market(s)

Healthcare vendors, other executives in healthcare and pharmaceuticals

Industry/Entity Type

Pharmaceutical

Contact Information for Business Card

See attachment

Font styles to use
Serif
Sans Serif

Colors

Designer to choose colors to be used in the design.

```html
<!DOCTYPE html>
<html lang="en">
<head>
<meta charset="utf-8">
<title>Corvale Therapeutics – Business Card</title>
<link href="https://fonts.googleapis.com/css2?family=Open+Sans:wght@300;400;700&display=swap" rel="stylesheet">
<style>
  :root {
    --canvas: #e9ebea;
    --brand-green: #4aab77;
    --name-green: #2f9a55;
    --teal: #36b8c8;
    --ring-green: #5cc08a;
    --olive: #b4b24a;
    --ink: #2b2b2b;
    --card-white: #fbfbfa;
    --faint: rgba(120, 200, 200, 0.16);
  }
  * { box-sizing: border-box; margin: 0; padding: 0; }
  html, body { width: 1200px; height: 1000px; overflow: hidden; }
  body {
    background: var(--canvas);
    font-family: "Open Sans", Arial, sans-serif;
    position: relative;
  }
  .card {
    position: absolute;
    width: 560px;
    height: 320px;
    border-radius: 18px;
    overflow: hidden;
    box-shadow: 0 10px 28px rgba(0,0,0,0.18);
  }
  /* Front */
  .card--front { left: 70px; top: 90px; background: var(--brand-green); }
  .front-lockup {
    position: absolute; left: 0; right: 0; top: 0; bottom: 0;
    display: flex; align-items: center; justify-content: center; gap: 22px;
  }
  .front-lockup .brand-dot {
    width: 96px; height: 96px; border-radius: 50%;
    border: 3px solid #fff;
  }
  .front-lockup .brand-name {
    color: #fff; font-weight: 300; font-size: 34px; line-height: 1.1;
  }
  /* Back */
  .card--back { left: 570px; top: 560px; background: var(--card-white); }
  .back-decoration {
    position: absolute; left: 70px; top: -10px;
    width: 340px; height: 340px; border-radius: 50%;
    border: 10px solid var(--faint);
  }
  .person {
    position: absolute; left: 36px; top: 150px;
  }
  .person__name {
    color: var(--name-green); font-weight: 700; font-size: 19px; letter-spacing: 0.5px;
  }
  .person__title { color: var(--ink); font-size: 13px; margin-top: 2px; }
  .contact {
    position: absolute; right: 30px; top: 28px; width: 190px;
    color: var(--ink); font-size: 12px; line-height: 1.4;
  }
  .contact__address { margin-bottom: 12px; }
  .contact__row { display: flex; align-items: center; gap: 6px; }
  .contact__row svg { width: 11px; height: 11px; flex: none; }
  .divider {
    position: absolute; left: 300px; right: 0; top: 190px;
    height: 1.5px; background: var(--olive);
  }
  .back-lockup {
    position: absolute; right: 28px; bottom: 40px;
    display: flex; align-items: center; gap: 14px;
  }
  .back-lockup .brand-dot {
    width: 66px; height: 66px; border-radius: 50%;
    border: 2px solid var(--ring-green);
  }
  .back-lockup .brand-name {
    color: var(--teal); font-weight: 300; font-size: 22px; line-height: 1.1;
  }
</style>
</head>
<body>
  <section class="card card--front" aria-label="Card front">
    <div class="front-lockup">
      <div class="brand-dot"></div>
      <div class="brand-name">Corvale<br>Therapeutics</div>
    </div>
  </section>

  <section class="card card--back" aria-label="Card back">
    <div class="back-decoration"></div>

    <div class="contact">
      <p class="contact__address">Corvale Therapeutics, LLC<br>118 W Linden Avenue<br>Fairview, GA 30650</p>
      <p class="contact__row">
        <svg viewBox="0 0 12 12"><path fill="#36b8c8" d="M2.5 1h2l1 2.5-1.3 1a6 6 0 0 0 3.3 3.3l1-1.3L11 7.5v2a1 1 0 0 1-1 1A9 9 0 0 1 1.5 2a1 1 0 0 1 1-1z"/></svg>
        555-210-4471 (Office)
      </p>
      <p class="contact__row">
        <svg viewBox="0 0 12 12"><path fill="#36b8c8" d="M2.5 1h2l1 2.5-1.3 1a6 6 0 0 0 3.3 3.3l1-1.3L11 7.5v2a1 1 0 0 1-1 1A9 9 0 0 1 1.5 2a1 1 0 0 1 1-1z"/></svg>
        555-382-6190 (Cell)
      </p>
      <p class="contact__row">
        <svg viewBox="0 0 12 12"><rect x="1" y="2.5" width="10" height="7" rx="1" fill="#36b8c8"/><path d="M1.5 3 6 6.5 10.5 3" stroke="#fff" stroke-width="1" fill="none"/></svg>
        dmarsh@corvalerx.com
      </p>
    </div>

    <div class="person">
      <p class="person__name">DANIEL MARSH</p>
      <p class="person__title">Senior Director of Marketing</p>
    </div>

    <div class="divider"></div>

    <div class="back-lockup">
      <div class="brand-dot"></div>
      <div class="brand-name">Corvale<br>Therapeutics</div>
    </div>
  </section>
</body>
</html>
```